App UI design needed! For a Password Management Tool

Need a design of a Windows desktop application which is a Password Management Tool, similar to Vaultkin, Brimlock or Keywell, with Business/Enterprise functionalities. Here attached are a few sample pages of Brimlock, and some sample pages of our app called Tessaly. We certainly want to redesign our app.
We need: 1. The layout of the web: top banner, menu, main pane; 2. Form style, main form and sub forms; 3. List style; 4 Fonts and buttons; 5. Logo.
The design should look professional, can attract business customers as well as individual users, and present a strong sense of “Security”. The look and feel should differentiate from well-known products like Vaultkin, Brimlock, Keywell, etc.

```html
<!DOCTYPE html>
<html lang="en">
<head>
<meta charset="utf-8">
<title>Tessaly – Web Logins</title>
<link href="https://fonts.googleapis.com/css2?family=Inter:wght@400;500;600&display=swap" rel="stylesheet">
<style>
:root{
  --ink:#1d1f3a;
  --muted:#6b6f9a;
  --faint:#a3a7c2;
  --blue:#0a8ff5;
  --blue-dark:#0b78e0;
  --panel:#eef0fb;
  --search:#eaecfb;
  --white:#ffffff;
  --line:#dfe1ec;
  --green:#2ee59d;
  --navy:#1f2350;
  --row:#eef0fb;
}
*{box-sizing:border-box;margin:0;padding:0}
html,body{width:1200px;height:750px;overflow:hidden;background:var(--white);font-family:"Inter",sans-serif;color:var(--ink)}
.app{position:relative;width:1200px;height:750px}
.abs{position:absolute}
.brand{left:16px;top:33px;width:152px;height:33px;background:var(--ink);color:var(--white);font-size:18px;font-weight:600;display:flex;align-items:center;gap:8px;padding-left:8px}
.brand-dot{width:16px;height:16px;border-radius:50%;background:var(--blue)}
.search{left:240px;top:30px;width:480px;height:39px;background:var(--search);border-radius:7px;display:flex;align-items:center;justify-content:space-between;padding:0 14px 0 26px;font-size:13px;color:var(--faint)}
.avatar{left:1106px;top:32px;width:36px;height:36px;border-radius:50%;border:2px solid var(--blue);background:linear-gradient(135deg,#5a4a42,#2b2320)}
.nav-item{left:22px;display:flex;align-items:center;gap:14px;font-size:14px;font-weight:500;height:20px}
.nav-active{left:10px;top:309px;width:220px;height:51px;border:1px solid var(--blue);border-radius:7px;background:var(--panel)}
.version{left:16px;top:728px;font-size:11px;color:var(--faint)}
.main{left:240px;top:101px;width:960px;height:649px;background:var(--panel);border-radius:8px 0 0 0}
.page-title{left:267px;top:120px;font-size:19px;font-weight:500}
.page-sub{left:267px;top:146px;font-size:13px;color:var(--muted)}
.btn-new{left:1046px;top:114px;width:113px;height:45px;border-radius:7px;background:var(--blue);color:var(--white);font-size:14px;font-weight:600;display:flex;align-items:center;justify-content:center;gap:8px;box-shadow:0 6px 14px rgba(10,143,245,.3)}
.card{left:267px;top:182px;width:896px;height:546px;background:var(--white);border-radius:8px}
.lists-title{left:291px;top:203px;font-size:19px;font-weight:500}
.count{left:647px;top:208px;font-size:11px;color:var(--muted)}
.pager{left:1045px;top:205px;font-size:11px;color:var(--muted);display:flex;align-items:center;gap:6px}
.pager-box{width:28px;height:22px;background:var(--search);border-radius:4px;display:flex;align-items:center;justify-content:center}
.check{width:17px;height:17px;border:1.5px solid #b9bce0;border-radius:4px;background:var(--white)}
.th{font-size:13px;font-weight:500;top:250px}
.row-hl{left:272px;top:345px;width:876px;height:51px;background:var(--row);border-radius:6px}
.cell{font-size:13px}
.name{font-weight:500}
.mark{width:22px;height:22px;border-radius:50%}
.divider{left:292px;width:861px;height:1px;background:var(--line)}
.tooltip{left:984px;top:393px;width:57px;height:25px;background:var(--navy);color:var(--white);border-radius:4px;font-size:12px;display:flex;align-items:center;justify-content:center}
</style>
</head>
<body>
<div class="app">
  <div class="abs brand"><span class="brand-dot"></span>Tessaly</div>
  <div class="abs search">Find something...
    <svg width="18" height="18" viewBox="0 0 18 18" fill="none" stroke="#a3a7c2" stroke-width="1.5"><circle cx="8" cy="8" r="6"/><path d="M12.5 12.5l4 4"/></svg>
  </div>
  <svg class="abs" style="left:950px;top:37px" width="24" height="26" viewBox="0 0 24 26"><path d="M12 3c-4 0-6 3-6 7v5l-2 3h16l-2-3v-5c0-4-2-7-6-7z" fill="#0a8ff5"/><circle cx="12" cy="21" r="2.5" fill="#0a8ff5"/><circle cx="18" cy="5" r="3" fill="#2ee59d"/></svg>
  <svg class="abs" style="left:1032px;top:39px" width="22" height="22" viewBox="0 0 24 24"><path fill="#0a8ff5" d="M19.4 13a7.5 7.5 0 000-2l2.1-1.6-2-3.5-2.5 1a7.6 7.6 0 00-1.7-1L14.9 3h-4l-.4 2.6a7.6 7.6 0 00-1.7 1l-2.5-1-2 3.5L6.5 11a7.5 7.5 0 000 2l-2.1 1.6 2 3.5 2.5-1a7.6 7.6 0 001.7 1l.4 2.9h4l.4-2.6a7.6 7.6 0 001.7-1l2.5 1 2-3.5zM12.9 15.5a3.5 3.5 0 110-7 3.5 3.5 0 010 7z"/></svg>
  <div class="abs avatar" role="img" aria-label="User profile photo"></div>
  <svg class="abs" style="left:1153px;top:47px" width="10" height="7" viewBox="0 0 10 7"><path d="M0 0h10L5 6z" fill="#2ee59d"/></svg>

  <div class="abs nav-active"></div>
  <div class="abs nav-item" style="top:120px"><svg width="20" height="20" viewBox="0 0 20 20"><rect x="1" y="1" width="7" height="9" rx="2" fill="#0a8ff5"/><rect x="1" y="12" width="7" height="7" rx="2" fill="#2ee59d"/><rect x="10" y="1" width="8" height="18" rx="2" fill="#1d1f3a"/></svg>Dashboard</div>
  <div class="abs nav-item" style="top:171px"><svg width="20" height="20" viewBox="0 0 20 20"><circle cx="10" cy="6" r="4" fill="#0a8ff5"/><path d="M3 18c0-4 3-6 7-6s7 2 7 6z" fill="#0a8ff5"/></svg>Users</div>
  <div class="abs nav-item" style="top:222px"><svg width="20" height="20" viewBox="0 0 20 20"><circle cx="7" cy="7" r="3.5" fill="#0a8ff5"/><path d="M1 17c0-4 3-5.5 6-5.5s6 1.5 6 5.5z" fill="#0a8ff5"/><circle cx="14" cy="5" r="2.5" fill="#2ee59d"/><path d="M14 9c3 0 5 1.5 5 4h-4z" fill="#2ee59d"/></svg>Teams</div>
  <div class="abs nav-item" style="top:272px"><svg width="20" height="20" viewBox="0 0 20 20"><rect x="1" y="1" width="9" height="7" rx="2" fill="#0a8ff5"/><rect x="10" y="12" width="9" height="7" rx="2" fill="#2ee59d"/><path d="M5 8v6h5" stroke="#1d1f3a" stroke-width="1.5" fill="none"/></svg>Client Containers</div>
  <div class="abs nav-item" style="top:323px"><svg width="20" height="20" viewBox="0 0 20 20"><circle cx="10" cy="10" r="8.5" fill="#2ee59d"/><path d="M1.5 10h17M10 1.5c-3 3-3 14 0 17M10 1.5c3 3 3 14 0 17M3 6h14M3 14h14" stroke="#0a8ff5" stroke-width="1.4" fill="none"/></svg>Web Logins</div>
  <div class="abs nav-item" style="top:373px"><svg width="20" height="20" viewBox="0 0 20 20"><path d="M3 1h10l4 4v14H3z" fill="#0a8ff5"/><path d="M6 10h8M6 13h8M6 16h5" stroke="#1d1f3a" stroke-width="1.3"/></svg>Reports</div>
  <div class="abs version">Version 2.3.4</div>

  <div class="abs main"></div>
  <div class="abs page-title">Web Logins</div>
  <div class="abs page-sub">Showing details of all the web logins saved in your system</div>
  <div class="abs btn-new"><svg width="13" height="13" viewBox="0 0 13 13"><path d="M6.5 0v13M0 6.5h13" stroke="#fff" stroke-width="1.8"/></svg>New</div>

  <div class="abs card"></div>
  <div class="abs lists-title">Lists</div>
  <div class="abs count">Showing 1-10 of 354 items</div>
  <div class="abs pager">Page <span class="pager-box">1</span> / 36</div>

  <div class="abs check" style="left:292px;top:249px"></div>
  <div class="abs th" style="left:329px">Name</div>
  <div class="abs th" style="left:518px">User name</div>
  <div class="abs th" style="left:749px">Login page URL</div>

  <div class="abs row-hl"></div>

  <div class="abs check" style="left:292px;top:305px"></div>
  <div class="abs mark" style="left:328px;top:302px;background:#1877f2"></div>
  <div class="abs cell name" style="left:360px;top:305px">Chatterly</div>
  <div class="abs cell" style="left:518px;top:305px">mara.lin@inboxly.com</div>
  <div class="abs cell" style="left:751px;top:305px">https://www.chatterly.com</div>

  <div class="abs check" style="left:292px;top:361px"></div>
  <div class="abs mark" style="left:328px;top:358px;background:#1d1f3a"></div>
  <div class="abs cell name" style="left:361px;top:361px">Codeforge</div>
  <div class="abs cell" style="left:518px;top:361px">mara.lin@inboxly.com</div>
  <div class="abs cell" style="left:751px;top:360px">https://www.codeforge.com/login</div>
  <svg class="abs" style="left:1006px;top:360px" width="18" height="18" viewBox="0 0 18 18" fill="none" stroke="#1d1f3a" stroke-width="1.5"><path d="M1 5V1h4M13 1h4v4M17 13v4h-4M5 17H1v-4"/><circle cx="6.5" cy="9" r="2"/><path d="M8.5 9H13v2M11 9v1.5"/></svg>
  <svg class="abs" style="left:1065px;top:359px" width="18" height="18" viewBox="0 0 18 18" fill="none" stroke="#1d1f3a" stroke-width="1.6"><path d="M8 2H2v14h14v-6"/><path d="M14 1.5l2.5 2.5L9 11.5H6.5V9z"/></svg>
  <svg class="abs" style="left:1112px;top:359px" width="15" height="17" viewBox="0 0 15 17"><path d="M0 2.5h15M5 2.5V0.8h5v1.7" stroke="#1d1f3a" stroke-width="1.6" fill="none"/><path d="M1.5 4h12l-1 13h-10z" fill="#1d1f3a"/><path d="M5.5 6.5v8M9.5 6.5v8" stroke="#fff" stroke-width="1.2"/></svg>
  <svg class="abs" style="left:1030px;top:372px" width="14" height="20" viewBox="0 0 14 20"><path d="M1 1v15l4-3.5 2.5 5.5 2.2-1-2.5-5.3H13z" fill="#fff" stroke="#1d1f3a" stroke-width="1"/></svg>
  <div class="abs tooltip">Open</div>

  <div class="abs check" style="left:292px;top:418px"></div>
  <div class="abs mark" style="left:328px;top:415px;background:#ea4335"></div>
  <div class="abs cell name" style="left:360px;top:418px">Searchly</div>
  <div class="abs cell" style="left:518px;top:418px">mara.lin@inboxly.com</div>
  <div class="abs cell" style="left:751px;top:418px">https://portal.kelvora.com</div>

  <div class="abs divider" style="top:461px"></div>

  <div class="abs check" style="left:292px;top:488px"></div>
  <div class="abs mark" style="left:328px;top:485px;background:#1877f2"></div>
  <div class="abs cell name" style="left:360px;top:488px">Chatterly</div>
  <div class="abs cell" style="left:518px;top:488px">mara.lin12@inboxly.com</div>
  <div class="abs cell" style="left:751px;top:488px">https://www.chatterly.com</div>

  <div class="abs divider" style="top:527px"></div>

  <div class="abs check" style="left:292px;top:546px"></div>
  <div class="abs mark" style="left:328px;top:543px;background:#f6b300"></div>
  <div class="abs cell name" style="left:360px;top:546px">Shopway</div>
  <div class="abs cell" style="left:518px;top:546px">mara.lin@inboxly.com</div>
  <div class="abs cell" style="left:751px;top:546px">https://www.shopway.com</div>
</div>
</body>
</html>
```